Aldercrest Chiropractic Rehabilitation and Wellness
Business Card, Portfolio Folder, Stationary, Postcard
Simple
Marlow Tenney
Doctor of Chiropractic
518 Verbena Ridge Avenue
Larkfield, OR 97402
marlow@alderbrook.com
www.alderbrook.com
Fonts are TrajanPro and Corbel
Logo and URL or just logo
Logo
jpg Logo

```html
<!DOCTYPE html>
<html lang="en">
<head>
<meta charset="utf-8">
<title>Aldercrest Chiropractic – Business Card</title>
<link href="https://fonts.googleapis.com/css2?family=Cinzel:wght@400;600&family=Open+Sans:wght@400;600&display=swap" rel="stylesheet">
<style>
  :root {
    --stage: #eeeae4;
    --card: #ffffff;
    --blue: #1b5fb5;
    --blue-deep: #0f3f8c;
    --blue-light: #3b86d9;
    --green: #7cc242;
    --text-white: #ffffff;
    --ink-blue: #1d4f9c;
  }
  * { box-sizing: border-box; margin: 0; padding: 0; }
  html, body { width: 1200px; height: 1075px; overflow: hidden; }
  body {
    background: var(--stage);
    font-family: "Open Sans", sans-serif;
    position: relative;
  }
  .card {
    position: absolute;
    left: 180px;
    width: 840px;
    height: 480px;
    background: var(--card);
    border-radius: 26px;
    overflow: hidden;
    box-shadow: 0 6px 18px rgba(0,0,0,0.12);
  }
  .card--front { top: 40px; }
  .card--back { top: 555px; }

  .front-panel { position: absolute; inset: 0; }

  .brand {
    position: absolute;
    left: 40px;
    top: 130px;
    width: 300px;
    text-align: center;
    color: var(--ink-blue);
    font-family: "Cinzel", serif;
    font-weight: 600;
  }
  .brand__dot {
    width: 86px; height: 86px; border-radius: 50%;
    background: var(--blue);
    margin: 0 auto 22px;
  }
  .brand__name { font-size: 38px; letter-spacing: 2px; line-height: 1.05; }
  .brand__sub { font-size: 22px; letter-spacing: 1px; margin-top: 4px; }
  .brand__tag { font-size: 13px; letter-spacing: 1px; margin-top: 8px; }

  .identity {
    position: absolute;
    right: 40px;
    top: 38px;
    text-align: right;
    color: var(--text-white);
    font-family: "Cinzel", serif;
  }
  .identity__name { font-size: 36px; font-weight: 600; letter-spacing: 1px; }
  .identity__title { font-size: 17px; letter-spacing: 1px; margin-top: 2px; }

  .contact {
    position: absolute;
    right: 40px;
    top: 205px;
    list-style: none;
    color: var(--text-white);
    font-size: 21px;
  }
  .contact__row {
    display: flex;
    justify-content: flex-end;
    align-items: center;
    gap: 14px;
    height: 34px;
  }
  .contact__row--gap { margin-bottom: 14px; }
  .contact__icon { width: 22px; height: 22px; flex: none; }

  .back-brand {
    position: absolute;
    left: 0; right: 0;
    top: 110px;
    display: flex;
    flex-direction: column;
    align-items: center;
    color: var(--ink-blue);
    font-family: "Cinzel", serif;
    font-weight: 600;
  }
  .back-brand__dot {
    width: 150px; height: 150px; border-radius: 50%;
    background: var(--blue);
  }
  .back-brand__name { font-size: 26px; letter-spacing: 3px; margin-top: 18px; }
  .back-url {
    position: absolute;
    left: 0; right: 0; bottom: 70px;
    text-align: center;
    color: var(--ink-blue);
    font-family: "Cinzel", serif;
    font-weight: 600;
    font-size: 28px;
    letter-spacing: 1px;
  }
</style>
</head>
<body>

<section class="card card--front">
  <svg class="front-panel" width="840" height="480" viewBox="0 0 840 480">
    <defs>
      <radialGradient id="panelGlow" cx="0.55" cy="0.45" r="0.75">
        <stop offset="0" stop-color="#3b86d9"/>
        <stop offset="1" stop-color="#0f3f8c"/>
      </radialGradient>
    </defs>
    <path d="M 352 0 C 430 120, 300 320, 368 480 L 390 480 C 322 320, 452 120, 374 0 Z" fill="#7cc242"/>
    <path d="M 380 0 C 458 120, 328 320, 396 480 L 840 480 L 840 0 Z" fill="url(#panelGlow)"/>
  </svg>

  <div class="brand">
    <div class="brand__dot"></div>
    <div class="brand__name">ALDERCREST</div>
    <div class="brand__sub">CHIROPRACTIC</div>
    <div class="brand__tag">REHABILITATION AND WELLNESS</div>
  </div>

  <div class="identity">
    <div class="identity__name">MARLOW TENNEY</div>
    <div class="identity__title">DOCTOR OF CHIROPRACTIC</div>
  </div>

  <ul class="contact">
    <li class="contact__row">518 Verbena Ridge Avenue
      <svg class="contact__icon" viewBox="0 0 24 24"><path d="M12 3 L2 12 H5 V21 H10 V15 H14 V21 H19 V12 H22 Z" fill="#fff"/></svg>
    </li>
    <li class="contact__row contact__row--gap">Larkfield, OR 97402
      <span class="contact__icon"></span>
    </li>
    <li class="contact__row">(541) 555 0148
      <svg class="contact__icon" viewBox="0 0 24 24"><path d="M6 3 L9 3 L11 8 L8.5 10 C9.5 12.5 11.5 14.5 14 15.5 L16 13 L21 15 L21 18 C21 20 19 21 17 21 C9 20 4 15 3 7 C3 5 4 3 6 3 Z" fill="#fff"/></svg>
    </li>
    <li class="contact__row">marlow@alderbrook.com
      <svg class="contact__icon" viewBox="0 0 24 24"><circle cx="12" cy="12" r="9" fill="none" stroke="#fff" stroke-width="2"/><circle cx="12" cy="12" r="3.5" fill="none" stroke="#fff" stroke-width="2"/><path d="M15.5 9 V14 C15.5 16 19 16 19 12" fill="none" stroke="#fff" stroke-width="2"/></svg>
    </li>
    <li class="contact__row">www.alderbrook.com
      <svg class="contact__icon" viewBox="0 0 24 24"><circle cx="12" cy="12" r="9" fill="none" stroke="#fff" stroke-width="2"/><path d="M3 12 H21 M12 3 C8 8 8 16 12 21 M12 3 C16 8 16 16 12 21" fill="none" stroke="#fff" stroke-width="1.6"/></svg>
    </li>
  </ul>
</section>

<section class="card card--back">
  <div class="back-brand">
    <div class="back-brand__dot"></div>
    <div class="back-brand__name">ALDERCREST</div>
  </div>
  <div class="back-url">WWW.ALDERBROOK.COM</div>
</section>

</body>
</html>
```